Bref créative
Fjellbrinken Tannregulering Stationery
Orthodontic Clinic
Professional
Fjellbrinken Tannregulering
Kjeveortoped Stian Haugvik
Myrbakkvegen 128
Postboks 71 Kvernvika
5912 BERGEN
post@smilbrink.no
www.smilbrink.no
Telefon 55 83 17 62

```html
<!DOCTYPE html>
<html lang="no">
<head>
<meta charset="utf-8">
<title>Fjellbrinken Tannregulering – Stationery</title>
<link href="https://fonts.googleapis.com/css2?family=Open+Sans:wght@400;600&display=swap" rel="stylesheet">
<style>
:root{
  --blue:#1d6fb3;
  --green:#7cc242;
  --green-dark:#5aa82c;
  --ink:#555a60;
  --rule:#b9bec4;
  --paper:#ffffff;
  --backdrop:#e8e5e0;
}
*{margin:0;padding:0;box-sizing:border-box}
html,body{width:1200px;height:514px;overflow:hidden;background:var(--backdrop);font-family:"Open Sans",Arial,sans-serif;color:var(--ink)}
.canvas{position:relative;width:1200px;height:514px}
.sheet{position:absolute;background:var(--paper);box-shadow:0 2px 6px rgba(0,0,0,.18);overflow:hidden}
.letterhead{left:24px;top:22px;width:372px;height:470px}
.fax{left:412px;top:22px;width:372px;height:470px}
.card-front{left:804px;top:26px;width:180px;height:100px}
.card-back{left:996px;top:26px;width:180px;height:100px;background:linear-gradient(135deg,var(--green) 0%,var(--green-dark) 100%)}
.envelope{left:804px;top:200px;width:372px;height:292px}

.brand{position:absolute;display:flex;align-items:center;gap:6px}
.brand-dot{width:14px;height:14px;border-radius:50%;background:var(--blue);flex:none}
.brand-name{font-weight:600;color:var(--blue);font-size:10px;line-height:1.2;white-space:nowrap}
.brand-sub{position:absolute;font-size:5.5px;color:var(--green-dark);font-weight:600}
.letterhead .brand,.fax .brand{left:14px;top:14px}
.letterhead .brand-sub,.fax .brand-sub{left:34px;top:31px}

.address{position:absolute;left:14px;font-size:5.5px;line-height:1.5}
.letterhead .address,.fax .address{top:388px}
.footer-wave{position:absolute;left:0;bottom:0;width:372px;height:56px}
.web{position:absolute;font-size:6px;font-weight:600;color:var(--blue)}
.letterhead .web,.fax .web{right:14px;bottom:22px;color:#fff}

.fax-title{position:absolute;left:30px;top:70px;font-size:26px;font-weight:400;color:#333;letter-spacing:1px}
.fax-fields{position:absolute;left:30px;top:112px;width:312px;display:grid;grid-template-columns:1fr 1fr;column-gap:20px;row-gap:12px}
.field{border-bottom:1px solid var(--rule);font-size:6px;padding-bottom:2px;height:12px}
.fax-rule{position:absolute;left:30px;top:218px;width:312px;border-top:1px solid var(--rule)}
.fax-checks{position:absolute;left:30px;top:226px;width:312px;display:flex;justify-content:space-between;font-size:6px}
.check{display:flex;align-items:center;gap:4px}
.check::before{content:"";width:7px;height:7px;border:1px solid #777}

.card-front .brand{left:8px;top:9px;gap:4px}
.card-front .brand-name{font-size:7.5px}
.card-front .brand-dot{width:10px;height:10px}
.card-contact{position:absolute;left:10px;top:34px;font-size:4.6px;line-height:1.5}
.card-person{position:absolute;right:8px;top:50px;text-align:right;font-size:5px;line-height:1.5}
.card-person strong{color:var(--blue);font-size:6px;font-weight:600}
.card-wave{position:absolute;left:0;bottom:0;width:180px;height:24px}
.card-back-name{position:absolute;left:0;right:0;top:40px;text-align:center;color:#fff;font-weight:600;font-size:9px;white-space:nowrap}
.card-back .web{left:0;right:0;bottom:12px;text-align:center;color:#fff}

.envelope .brand{left:14px;top:16px}
.envelope .brand-sub{left:34px;top:33px}
.envelope .address{top:80px;font-size:5px}
.env-lines{position:absolute;left:196px;top:78px;width:156px}
.env-lines span{display:block;border-bottom:1px solid var(--rule);height:16px}
.envelope .web{right:20px;top:150px}
.env-flap{position:absolute;left:0;top:160px;width:372px;height:132px}
</style>
</head>
<body>
<main class="canvas">

  <section class="sheet letterhead" aria-label="Letterhead">
    <div class="brand"><span class="brand-dot"></span><span class="brand-name">Fjellbrinken Tannregulering</span></div>
    <div class="brand-sub">Kjeveortoped Stian Haugvik</div>
    <div class="address">Myrbakkvegen 128 · Postboks 71 Kvernvika<br>5912 BERGEN<br>Telefon 55 83 17 62<br>post@smilbrink.no</div>
    <svg class="footer-wave" viewBox="0 0 372 56" preserveAspectRatio="none">
      <path d="M0 44 C120 40 250 26 372 4 L372 56 L0 56Z" fill="var(--green)"/>
      <path d="M0 50 C130 48 260 36 372 16 L372 56 L0 56Z" fill="var(--blue)"/>
    </svg>
    <div class="web">www.smilbrink.no</div>
  </section>

  <section class="sheet fax" aria-label="Fax cover sheet">
    <div class="brand"><span class="brand-dot"></span><span class="brand-name">Fjellbrinken Tannregulering</span></div>
    <div class="brand-sub">Kjeveortoped Stian Haugvik</div>
    <h1 class="fax-title">FAX</h1>
    <div class="fax-fields">
      <div class="field">To:</div><div class="field">From:</div>
      <div class="field">Fax:</div><div class="field">Pages:</div>
      <div class="field">Phone:</div><div class="field">Date:</div>
      <div class="field">Re:</div><div class="field">CC:</div>
    </div>
    <div class="fax-rule"></div>
    <div class="fax-checks">
      <span class="check">Urgent</span><span class="check">For Review</span><span class="check">Please Comment</span><span class="check">Please Reply</span><span class="check">Please Recycle</span>
    </div>
    <div class="address">Myrbakkvegen 128 · Postboks 71 Kvernvika<br>5912 BERGEN<br>Telefon 55 83 17 62<br>post@smilbrink.no</div>
    <svg class="footer-wave" viewBox="0 0 372 56" preserveAspectRatio="none">
      <path d="M0 44 C120 40 250 26 372 4 L372 56 L0 56Z" fill="var(--green)"/>
      <path d="M0 50 C130 48 260 36 372 16 L372 56 L0 56Z" fill="var(--blue)"/>
    </svg>
    <div class="web">www.smilbrink.no</div>
  </section>

  <section class="sheet card-front" aria-label="Business card front">
    <div class="brand"><span class="brand-dot"></span><span class="brand-name">Fjellbrinken Tannregulering</span></div>
    <div class="card-contact">Myrbakkvegen 128<br>5912 BERGEN<br>Tlf 55 83 17 62<br>post@smilbrink.no</div>
    <div class="card-person"><strong>Stian Haugvik</strong><br>Kjeveortoped</div>
    <svg class="card-wave" viewBox="0 0 180 24" preserveAspectRatio="none">
      <path d="M0 14 C60 14 120 10 180 2 L180 24 L0 24Z" fill="var(--green)"/>
      <path d="M0 19 C60 19 120 16 180 9 L180 24 L0 24Z" fill="var(--blue)"/>
    </svg>
  </section>

  <section class="sheet card-back" aria-label="Business card back">
    <div class="card-back-name">Fjellbrinken Tannregulering</div>
    <div class="web">www.smilbrink.no</div>
  </section>

  <section class="sheet envelope" aria-label="Envelope">
    <div class="brand"><span class="brand-dot"></span><span class="brand-name">Fjellbrinken Tannregulering</span></div>
    <div class="brand-sub">Kjeveortoped Stian Haugvik</div>
    <div class="address">Myrbakkvegen 128<br>Postboks 71 Kvernvika<br>5912 BERGEN<br>Tlf 55 83 17 62<br>post@smilbrink.no</div>
    <div class="env-lines"><span></span><span></span><span></span><span></span></div>
    <div class="web">www.smilbrink.no</div>
    <svg class="env-flap" viewBox="0 0 372 132" preserveAspectRatio="none">
      <rect width="372" height="132" fill="#f1f2f3"/>
      <path d="M0 0 L186 104 L372 0 L372 10 L186 114 L0 10Z" fill="var(--green)"/>
      <path d="M0 10 L186 114 L372 10 L372 18 L186 122 L0 18Z" fill="var(--blue)"/>
      <path d="M0 0 L186 104 L372 0Z" fill="#ffffff"/>
      <circle cx="186" cy="58" r="10" fill="var(--blue)"/>
    </svg>
  </section>

</main>
</body>
</html>
```